Die Designerin hat meine Vorstellungen am besten verstanden und umgesetzt. Sie war mir gegenüber sehr verständnisvoll und entgegenkommend. Die Kommunikation mit ihr war sehr erfreulich und sympathisch. Bei meinem nächsten Projekt werde ich mich zuerst an sie wenden.

```html
<!DOCTYPE html>
<html lang="de">
<head>
<meta charset="utf-8">
<title>Mein unfassbarer Sommer in Sietebühl – Buchumschlag</title>
<link rel="stylesheet" href="https://fonts.googleapis.com/css2?family=PT+Serif:wght@400;700&display=swap">
<style>
  :root {
    --stage: #ddb043;
    --paper: #eef0f1;
    --paper-shade: #e4e6e8;
    --wash: #bcdcec;
    --accent-orange: #e0a020;
    --blue-bright: #3ab9e9;
    --blue-soft: #6fc0d8;
    --blue-mid: #33a6d8;
    --blue-deep: #1a8ccd;
  }
  * { box-sizing: border-box; margin: 0; padding: 0; }
  html, body {
    width: 1200px;
    height: 1055px;
    overflow: hidden;
    background: var(--stage);
  }
  .canvas {
    position: relative;
    width: 1200px;
    height: 1055px;
  }
  .cover {
    position: absolute;
    left: 189px;
    top: 88px;
    width: 593px;
    height: 880px;
    background: var(--paper);
    overflow: hidden;
    font-family: "PT Serif", serif;
    text-align: center;
  }
  .cover__wash {
    position: absolute;
    inset: 0;
    width: 100%;
    height: 100%;
  }
  .cover__label {
    position: absolute;
    top: 16px;
    left: 0;
    right: 0;
    font-size: 17px;
    font-weight: 700;
    letter-spacing: 4px;
    color: var(--accent-orange);
  }
  .cover__title {
    position: absolute;
    top: 78px;
    left: 0;
    right: 0;
    font-weight: 700;
    font-size: 50px;
    letter-spacing: 7px;
    line-height: 92px;
  }
  .cover__title span { display: block; }
  .title-mein { color: var(--blue-bright); }
  .title-unfassbarer { color: var(--blue-soft); }
  .title-sommer { color: var(--blue-mid); }
  .title-ort { color: var(--blue-deep); word-spacing: 14px; }
  .cover__art {
    position: absolute;
    left: 60px;
    top: 440px;
    width: 470px;
    height: 340px;
  }
  .cover__author {
    position: absolute;
    top: 802px;
    left: 0;
    right: 0;
    font-size: 24px;
    font-weight: 700;
    letter-spacing: 6px;
    color: var(--blue-deep);
  }
  .spine {
    position: absolute;
    left: 904px;
    top: 88px;
    width: 107px;
    height: 880px;
    background: var(--paper-shade);
    overflow: hidden;
    font-family: "PT Serif", serif;
  }
  .spine__title {
    position: absolute;
    top: 56px;
    left: 50%;
    transform: translateX(-50%);
    writing-mode: vertical-rl;
    font-size: 28px;
    font-weight: 700;
    letter-spacing: 2px;
    color: var(--blue-deep);
    white-space: nowrap;
  }
  .spine__foot {
    position: absolute;
    left: 0;
    right: 0;
    bottom: 0;
    height: 96px;
    background: var(--wash);
    display: flex;
    flex-direction: column;
    align-items: center;
    justify-content: center;
    font-size: 15px;
    line-height: 22px;
    color: #f4f8fa;
    text-transform: uppercase;
    letter-spacing: 1px;
  }
</style>
</head>
<body>
<main class="canvas">
  <section class="cover">
    <svg class="cover__wash" viewBox="0 0 593 880" aria-hidden="true">
      <defs>
        <linearGradient id="washTop" x1="0" y1="0" x2="1" y2="1">
          <stop offset="0" stop-color="#cfe6f1"/>
          <stop offset="1" stop-color="#a9d3e8"/>
        </linearGradient>
        <linearGradient id="washBottom" x1="0" y1="0" x2="1" y2="1">
          <stop offset="0" stop-color="#c5e2ef"/>
          <stop offset="1" stop-color="#deeef5"/>
        </linearGradient>
      </defs>
      <path d="M240 0 H593 V110 C560 90 530 60 470 50 C400 40 330 60 290 30 C270 15 255 8 240 0 Z" fill="url(#washTop)"/>
      <path d="M0 790 C40 800 70 830 130 850 C170 865 200 872 240 880 H0 Z" fill="url(#washBottom)"/>
    </svg>
    <p class="cover__label">ROMAN</p>
    <h1 class="cover__title">
      <span class="title-mein">Mein</span>
      <span class="title-unfassbarer">unfassbarer</span>
      <span class="title-sommer">Sommer</span>
      <span class="title-ort">in Sietebühl</span>
    </h1>
    <svg class="cover__art" viewBox="0 0 470 340" role="img" aria-label="Illustration: eine Person mit Helm fährt auf einem blauen Motorroller mit Pflanzen und Büschen vor einem pastellfarbenen Kreis">
      <defs>
        <radialGradient id="artGlow" cx="0.5" cy="0.5" r="0.5">
          <stop offset="0" stop-color="#f4d6d2"/>
          <stop offset="0.7" stop-color="#e9e0dc"/>
          <stop offset="1" stop-color="#dfeaf0"/>
        </radialGradient>
        <linearGradient id="artBody" x1="0" y1="0" x2="1" y2="1">
          <stop offset="0" stop-color="#f3d66c"/>
          <stop offset="0.55" stop-color="#7cc0e4"/>
          <stop offset="1" stop-color="#2e6fbf"/>
        </linearGradient>
      </defs>
      <circle cx="250" cy="150" r="175" fill="url(#artGlow)" opacity="0.8"/>
      <rect x="30" y="20" width="380" height="300" rx="120" fill="url(#artBody)" opacity="0.55"/>
    </svg>
    <p class="cover__author">KONRAD WEILMANN</p>
  </section>

  <aside class="spine">
    <p class="spine__title">Mein unfassbarer Sommer in Sietebühl</p>
    <div class="spine__foot">
      <span>Konrad</span>
      <span>Weilmann</span>
    </div>
  </aside>
</main>
</body>
</html>
```